Service Proposal brochure

I have a list of services, references and details I can provide to create the service proposal from.

Target Market(s)

Project Managers in the Construction/Electrical Field Industry

Industry/Entity Type

Construction/Electrical Industry

Font styles to use
Serif

Colors
0054AA
0677BA
7BADD7
CADEEF
E8F1F8
FFF300
FFF600
FEFA6F
FFFEC7
FFFEE8

Requirements
Must have
• High vocabulary
Nice to have
• Creativity in the details of service work and layout of the brochure
Should not have
• So much wording that it becomes boring for the consumer

```html
<!DOCTYPE html>
<html lang="en">
<head>
<meta charset="utf-8">
<title>Service Proposal Form</title>
<link rel="stylesheet" href="https://fonts.googleapis.com/css2?family=Krona+One&family=Montserrat:wght@500;600;700&family=Roboto+Condensed:wght@800&display=swap">
<style>
:root{
  --blue-deep:#0054AA;
  --blue-mid:#0677BA;
  --blue-soft:#7BADD7;
  --blue-pale:#CADEEF;
  --blue-mist:#E8F1F8;
  --yellow:#FFF300;
  --yellow-bright:#FFF600;
  --ink:#1d1d1f;
  --white:#ffffff;
}
*{margin:0;padding:0;box-sizing:border-box}
html,body{width:912px;height:1200px;overflow:hidden}
body{font-family:"Montserrat",Arial,sans-serif;color:var(--ink);background:#f3f5f8}
.sheet{position:relative;width:912px;height:1200px;overflow:hidden;
  background:linear-gradient(160deg,#ffffff 0%,#eef1f5 45%,#ffffff 70%,#eef1f5 100%)}
.masthead{position:absolute;left:0;top:0;width:912px;height:254px}
.title{position:absolute;left:59px;top:48px;color:var(--white);font-family:"Krona One",Arial,sans-serif;line-height:1;font-weight:400}
.title .line{display:block;font-size:45px;letter-spacing:-1px;margin-bottom:7px}
.title .sub{display:flex;align-items:center;gap:15px;margin-top:6px}
.title .sub span{color:var(--yellow);font-size:28px}
.title .sub i{display:block;height:2px;background:var(--yellow);width:83px}
.title .sub i.long{width:107px}
.section-head{position:absolute;left:48px;display:flex;align-items:center}
.section-head .tab{background:var(--blue-deep);color:var(--white);height:45px;display:flex;align-items:center;gap:14px;padding:0 24px 0 10px;font-size:27px;font-weight:600}
.section-head .rule{position:absolute;left:0;bottom:0;width:812px;height:2px;background:var(--blue-deep)}
.section-head svg{width:34px;height:34px}
.references{position:absolute;left:48px;top:349px;width:830px}
.ref{margin-bottom:10px}
.ref h3{font-size:17px;font-weight:700;line-height:1.25}
.ref p{font-size:14px;font-weight:500;line-height:1.35;white-space:nowrap}
.services{position:absolute;top:672px;left:48px;width:820px;display:flex}
.services ul{list-style:none}
.services .col-a{width:331px}
.services .col-b{width:356px}
.services li{position:relative;padding-left:18px;font-size:14.4px;font-weight:600;line-height:19px;margin-bottom:9.4px}
.services li::before{content:"";position:absolute;left:0;top:5px;width:10px;height:10px;border-radius:50%;background:var(--blue-deep)}
.services li::after{content:"";position:absolute;left:3.3px;top:7px;width:2.5px;height:4.5px;border:solid var(--white);border-width:0 1.4px 1.4px 0;transform:rotate(45deg)}
.services .brand{font-weight:500}
.cta{position:absolute;left:0;top:1004px;width:912px;text-align:center}
.cta span{display:inline-block;font-family:"Roboto Condensed",Arial,sans-serif;font-weight:800;font-size:38px;color:var(--blue-deep);transform:scaleX(.89)}
.footer{position:absolute;left:0;top:1052px;width:912px;height:128px;background:linear-gradient(90deg,var(--blue-deep) 0%,var(--blue-mid) 50%,var(--blue-deep) 100%);color:var(--white);text-align:center}
.icons{display:flex;justify-content:center;gap:9px;margin-top:16px}
.icons svg{width:20px;height:20px}
.footer p{font-size:14px;font-weight:600;line-height:18.5px}
.footer .lead{margin-top:5px}
.legal{position:absolute;left:0;top:1180px;width:912px;height:20px;background:var(--yellow-bright);text-align:center;font-size:10px;font-weight:600;letter-spacing:1.5px;color:var(--blue-deep);line-height:20px}
</style>
</head>
<body>
<main class="sheet">
  <header class="masthead">
    <svg width="912" height="254" viewBox="0 0 912 254">
      <defs>
        <linearGradient id="bandFill" x1="0" y1="0" x2="1" y2="0">
          <stop offset="0" stop-color="#0054AA"/>
          <stop offset="1" stop-color="#0677BA"/>
        </linearGradient>
        <linearGradient id="photoFill" x1="0" y1="0" x2="1" y2="0">
          <stop offset="0" stop-color="#b9bec6"/>
          <stop offset=".35" stop-color="#7BADD7"/>
          <stop offset="1" stop-color="#2f6bb3"/>
        </linearGradient>
      </defs>
      <polygon points="0,4 578,4 492,219 0,219" fill="url(#bandFill)"/>
      <rect x="0" y="0" width="608" height="4" fill="#FFF300"/>
      <polygon points="583,0 606,0 499,235 480,235" fill="#FFF300"/>
      <g role="img" aria-label="Photo of electricians in hard hats and safety glasses on a job site">
        <polygon points="606,0 912,0 912,254 493,254" fill="url(#photoFill)"/>
        <polygon points="787,0 912,0 912,254 690,254" fill="#0054AA" opacity=".35"/>
      </g>
    </svg>
    <h1 class="title">
      <span class="line">SERVICE</span>
      <span class="line">PROPOSAL</span>
      <span class="sub"><i></i><span>FORM</span><i class="long"></i></span>
    </h1>
  </header>

  <div class="section-head" style="top:269px">
    <div class="tab">
      <svg viewBox="0 0 34 34" aria-hidden="true">
        <circle cx="9" cy="7" r="4" fill="#FFF300"/><path d="M3 19a6 6 0 0 1 12 0z" fill="#FFF300"/>
        <circle cx="25" cy="20" r="4" fill="#FFF300"/><path d="M19 32a6 6 0 0 1 12 0z" fill="#FFF300"/>
        <path d="M20 5a9 9 0 0 1 9 9" stroke="#FFF300" stroke-width="2.5" fill="none"/><path d="M26 13l3 3 3-4" stroke="#FFF300" stroke-width="2" fill="none"/>
        <path d="M14 30a9 9 0 0 1-9-9" stroke="#FFF300" stroke-width="2.5" fill="none"/>
      </svg>
      References
    </div>
    <div class="rule"></div>
  </div>

  <section class="references">
    <div class="ref">
      <h3>Redhill Crest University</h3>
      <p>• Dale Marsh I Director of Campus Engineering I dmarsh@rcu.edu I 909-555-0142</p>
      <p>• Colin Brandt I Construction &amp; Wayfinding Senior Projector Manger I cbrandt@rcu.edu I (951)-555-0176</p>
    </div>
    <div class="ref">
      <h3>Pine Hollow Valley Water District</h3>
      <p>• Owen Pratt I Director of Operations I owen.pratt@phvwd.org I (951) 555-0193-ext.263</p>
    </div>
    <div class="ref">
      <h3>Halvorsen Engineering</h3>
      <p>• Trevor Lind I Plant &amp; Facilities Maintenance Director</p>
    </div>
    <div class="ref">
      <h3>Mesa Grove School District</h3>
      <p>• Rafael Ortiz I Maintenance Supervisor I rafael_ortiz@mgjusd.us I (909) 555-0118</p>
    </div>
  </section>

  <div class="section-head" style="top:604px">
    <div class="tab">
      <svg viewBox="0 0 34 34" aria-hidden="true">
        <circle cx="13" cy="18" r="8" fill="none" stroke="#FFF300" stroke-width="5" stroke-dasharray="4 2.3"/>
        <circle cx="13" cy="18" r="3" fill="#FFF300"/>
        <path d="M25 4v8M31 4v8M28 12v20" stroke="#FFF300" stroke-width="3.5" fill="none" stroke-linecap="round"/>
      </svg>
      Service’s Include
    </div>
    <div class="rule"></div>
  </div>

  <section class="services">
    <ul class="col-a">
      <li>Power-Upgrade/ Additional</li>
      <li>Lighting-Upgrade/ additional/ retrofits</li>
      <li>Remodels</li>
      <li>Design Build &amp; Design assist</li>
      <li>Medium voltage</li>
      <li>New equipment</li>
      <li>Voltara Battery packs</li>
      <li>Generators and Automatic<br>Transfer Switches</li>
      <li>Preventive Maintenance and Testing<br>(ETCA 2 Certified)</li>
    </ul>
    <ul class="col-b">
      <li>Arch Flash/Coordination Study</li>
      <li>Title 24 commissioning and acceptance</li>
      <li>Fire Alarm – <span class="brand">Quiet Sentry, Brenner, Flarewell</span></li>
      <li>Security (Intrusion) – <span class="brand">Brenner, Ardent, Halewood,<br>AlertNet</span></li>
      <li>Security (Access Control) – <span class="brand">Keyforge &amp; Porta</span></li>
      <li>Security (Cameras) – <span class="brand">Lumiscope, Vista Live, Brenner</span></li>
      <li>Public Address – <span class="brand">Callway &amp; Orbit Audio</span></li>
      <li>Structured Cable – <span class="brand">Linecraft, Corden</span></li>
    </ul>
  </section>

  <p class="cta"><span>CALL US TODAY TO SCHEDULE AN APPOINTMENT!</span></p>

  <footer class="footer">
    <div class="icons" aria-hidden="true">
      <svg viewBox="0 0 20 20"><circle cx="10" cy="10" r="10" fill="#FFF300"/><path d="M10 4a4 4 0 0 0-4 4c0 3 4 8 4 8s4-5 4-8a4 4 0 0 0-4-4z" fill="#0054AA"/><circle cx="10" cy="8" r="1.5" fill="#FFF300"/></svg>
      <svg viewBox="0 0 20 20"><circle cx="10" cy="10" r="10" fill="#FFF300"/><path d="M6 5l2.5-.5 1.2 3-1.5 1a7 7 0 0 0 3.3 3.3l1-1.5 3 1.2-.5 2.5C10 14 6 10 6 5z" fill="#0054AA"/></svg>
      <svg viewBox="0 0 20 20"><circle cx="10" cy="10" r="10" fill="#FFF300"/><rect x="7" y="4.5" width="6" height="3" fill="#0054AA"/><rect x="5" y="8" width="10" height="5" rx="1" fill="#0054AA"/><rect x="7" y="11.5" width="6" height="4" fill="#0054AA" stroke="#FFF300" stroke-width=".8"/></svg>
      <svg viewBox="0 0 20 20"><circle cx="10" cy="10" r="10" fill="#FFF300"/><rect x="5" y="6.5" width="10" height="7" rx="1" fill="none" stroke="#0054AA" stroke-width="1.4"/><path d="M5.5 7l4.5 3.5L14.5 7" fill="none" stroke="#0054AA" stroke-width="1.4"/></svg>
      <svg viewBox="0 0 20 20"><circle cx="10" cy="10" r="10" fill="#FFF300"/><circle cx="10" cy="10" r="5.5" fill="none" stroke="#0054AA" stroke-width="1.2"/><ellipse cx="10" cy="10" rx="2.3" ry="5.5" fill="none" stroke="#0054AA" stroke-width="1.2"/><path d="M4.5 10h11" stroke="#0054AA" stroke-width="1.2"/></svg>
    </div>
    <p class="lead">Lorem ipsum dolor sit amet, consectetur</p>
    <p>adipiscing elit, sed do eiusmod tempor</p>
    <p>(123) 456 7890 I (123) 7890 654</p>
    <p>info@example.com I www.websiteurl.com</p>
  </footer>
  <div class="legal">CopyRight@2022</div>
</main>
</body>
</html>
```